Seriöser Briefkopf für Rechtsanwaltskanzlei
Zielgruppe
Rechtsanwaltskanzlei
Aufgabenstellung
Benötigt wird ein seriöser Briefkopf für eine Anwaltskanzlei. Er soll im Wesentlichen aus Typen bestehen, mit denen aber durchaus 'gespielt' werden soll (Groß- und Kleinschreibung, querstehend, angeschnitten o.Ä)
Folgender Inhalt muss untergebracht werden:
Rechtsanwaltskanzlei Kessenhagen
Rechtsanwalt Dipl.-Ing. Udo Kessenhagen
Rechtsanwalt Matthias Wendel
Der Briefkopf muss schwarz-weiß druckbar sein und beim Versenden per Fax müssen alle Daten gut lesbar bleiben (also keine Grautöne bei Tel-Nr. o.Ä.)
Der Briefkopf soll mit einem Drucker ausgedruckt werden, sodass keine Gestaltung bis zum Blattrand gehen darf.
Bitte keine Logos mit Paragrafen-Zeichen oder Justitia und nicht die Abkürzung RUK verwenden.
Keine - Einfach drauflos - Ich bin gespannt

```html
<!DOCTYPE html>
<html lang="de">
<head>
<meta charset="utf-8">
<title>Briefbogen Rechtsanwaltskanzlei Kessenhagen</title>
<link href="https://fonts.googleapis.com/css2?family=Crimson+Text&family=Tinos&display=swap" rel="stylesheet">
<style>
  :root {
    --ink: #111111;
    --rule: #555555;
    --paper: #ffffff;
  }
  html, body { margin: 0; padding: 0; overflow: hidden; background: var(--paper); }
  .sheet {
    position: relative;
    width: 849px;
    height: 1200px;
    overflow: hidden;
    background: var(--paper);
    color: var(--ink);
  }
  .letterhead { position: absolute; left: 80px; width: 673px; top: 44px; text-align: center; font-family: "Crimson Text", serif; }
  .firm-kind { font-size: 17px; line-height: 18px; letter-spacing: 1px; }
  .firm-name { font-size: 26px; line-height: 28px; letter-spacing: 3px; text-transform: uppercase; }
  .rule { position: absolute; left: 80px; width: 673px; height: 0; border-top: 0.8px solid var(--rule); }
  .rule--head { top: 95px; }
  .rule--foot { top: 1131px; }
  .partners { position: absolute; left: 80px; width: 673px; top: 100px; text-align: center; font-family: "Crimson Text", serif; font-size: 10px; line-height: 13px; }
  .sender-line { position: absolute; left: 80px; top: 197px; font-family: "Tinos", serif; font-size: 9.4px; }
  .recipient { position: absolute; left: 80px; top: 224px; font-family: "Tinos", serif; font-size: 15.6px; line-height: 20.5px; }
  .letter-body { position: absolute; left: 80px; top: 420px; width: 675px; font-family: "Tinos", serif; font-size: 15.6px; line-height: 20.1px; hyphens: auto; }
  .letter-body p { margin: 0 0 20.1px; }
  .footer { position: absolute; left: 80px; width: 673px; top: 1140px; text-align: center; font-family: "Crimson Text", serif; font-size: 10px; }
</style>
</head>
<body>
<main class="sheet">
  <header>
    <div class="letterhead">
      <div class="firm-kind">Rechtsanwaltskanzlei</div>
      <div class="firm-name">Kessenhagen</div>
    </div>
    <div class="rule rule--head"></div>
    <div class="partners">
      Rechtsanwalt Dipl.-Ing. Udo Kessenhagen<br>
      Rechtsanwalt Matthias Wendel
    </div>
  </header>

  <div class="sender-line">Rechtsanwaltskanzlei Kessenhagen · Haldenweg 14 · 04109 Leipzig</div>

  <address class="recipient" style="font-style:normal">
    Herr Harald Mustermann<br>
    Musterstraße 123<br>
    12345 Musterfelden
  </address>

  <section class="letter-body">
    <p>Sehr geehrter Herr Mustermann</p>
    <p>Asperio cor maio dic tem velesti sapit earionsedit, volendest vel eicil eturiti strum, ea quatur sed que corendita adis dest, sunt aut pores eos raecae vit iliatur alitatem velitatum, omni ius nem nis et pos int ut quiatiscitat dolloreserum expliqu isinullaccus consequam, officiaectur abo. Lit lit que peritio. Nam earum quid quas erferiore natemque et ut resenda ndemqui corero temperibusae commimossime cus venducitat incitiur alignis non reprati am eum faccat doluptae nonsenet verferatis nis sam, quia invelendebis ex eles perum sa qui con ratias conet quae. Nam cum sit et volectem quia di nimus.</p>
    <p>Um sus, cumet pre asitios simpel evendestion rem fugia aut alis et voluptatent rerion con nihillut labo. Sitin recaecto odissit ullessi de conem si aut velent verae latem eni simaio. Debita volest ad magnist lique num incide liquam rerorriorro dolor repta volupta ererat laborem quam que aliquo occum inversp eliquam nobitatum quatem eat unt ipiduciendi nest, autas consedi cum faccabo. Lut officiandi sinum aut magnatum fuga. Odignatum re comnihi liquat.<br>
    Piendis maiorum laccabo. Essiti sit, sequosam, optatio dolum rent velecuptas por sin etum, ut quae landelibusae velitatio intio conserrum et apicatur?</p>
    <p>Arum hillupta dolor abo. Lesto tem faccaborrum asimi, conseque proreperrum volori tet ut hil essitium remperit vendi dus eos es pratur, eaque nus, unt exerum sinveles volum quas aliqui repudi cum sunt es estemol uptati verum exerumq uuntis utem est quis volupta dempore non pellab ipient provid explic te conse molecti audande rferum et laccum sinctametur molorum et re il ium faccusam faccationet landae magnia quunt re laborerum aute di doluptas remporeped qui am quia con reperibea sin nus sam quasi officabo.</p>
    <p>Quiduntes dolest es eiusam dolorit iscitiuri nonseque solorio rercim rerchil et ium arum quam, similles et officiis molorescia volorep elitia que prorporum inci officto blaccab orumquis dolorit re sunt quo voluptae officti oresequae volorrum rerum endio.</p>
    <p>MfG</p>
  </section>

  <footer>
    <div class="rule rule--foot"></div>
    <div class="footer">Haldenweg 14 · 04109 Leipzig · Tel. 0341 55821-0 · Fax 0341 55821-46 · mail@kessenhagen-recht.de · www.kessenhagen-recht.de</div>
  </footer>
</main>
</body>
</html>
```